NEW Website DESIGN for Brightwell Panes & Stoneworks Company

Brand New website, contemporary, clean, visual (images), not busy. ATTACHED IS OUR LOG THAT YOU MUST USE.

The company is called Brightwell Panes & Stoneworks (BrightwellPS)
www.brightwellps.com
The website should be www.brightwellpns.com
one page for glass one page for solid surfaces www.brightwellpanesplashes.co.uk
www.brightwellstoneworkss.co.uk

Target Market(s)

Hotels, Commercial projects, Small focus on residential

Industry/Entity Type

Construction

Number of Pages Required

5+ page

Font styles to use
Sans Serif

Requirements
Must have
• COLOURS AS PER OUR LOGO - WHITE/YELLOW/GREY - WHITE BACK GROUND
• CLEAR SIMPLE NAVIGATION - MODER CLEAN CUT - DESIGN FEEL
• LATEST NAVIGATION FOR IMAGES and text to include per project details
• WORK/PROJECT AREA - NEWS AREA - TEAM AREA/ABOUT US/CONTACT US
• NEW PAGEwww.brightwellpanesplashes.co.uk - NEW PAGE www.brightwellstoneworkss.co.uk
• PLEASE COPY THIS TYPE OF TEMPALTE
• https://www.harlowmead.co.uk/project/grand-halls/
• MOBILE READY
• WORDPRESS
• MODERN IMAGES INCLUDING VELMARA KESTRIN AND GLASS PROJECTS
Nice to have
• NEW DESIGN MODER FRESH
• WEBSITES I LIKE THE TEMPLATE SHOULD BE LIKE THE WEBSITE BELOW
• https://www.harlowmead.co.uk/
Should not have
• NOT Old fashion template, not busy NAVIGATION
• NO BLACK
• NO DARK GREYS
• NOT LOTS OF YELLOW
• RESDENTIAL IMAGES

```html
<!DOCTYPE html>
<html lang="en">
<head>
<meta charset="utf-8">
<title>Contact Us – Brightwell Panes &amp; Stoneworks</title>
<link rel="stylesheet" href="https://fonts.googleapis.com/css2?family=Montserrat:wght@600;700&family=Lato:wght@400;700&display=swap">
<style>
:root{
  --yellow:#f7ec3b;
  --grey-text:#6e6e6e;
  --grey-dark:#3a3a3a;
  --grey-mark:#8a8a8a;
  --grey-line:#c9c9c9;
  --hero-a:#eceff2;
  --hero-b:#d3d9df;
  --hero-c:#c4cad1;
  --map-a:#f1efe8;
  --map-b:#e6e3d6;
  --footer:#4a4a4a;
  --white:#ffffff;
}
*{box-sizing:border-box;margin:0;padding:0}
html,body{width:1200px;height:1161px;overflow:hidden;background:var(--white)}
body{position:relative;font-family:'Lato',sans-serif;color:var(--grey-dark)}

.site-header{position:absolute;left:0;top:0;width:1200px;height:85px;background:var(--white);z-index:3;box-shadow:0 1px 3px rgba(0,0,0,.08)}
.brand-tab{position:absolute;left:140px;top:0;width:255px;height:126px;z-index:4}
.brand-tab svg{position:absolute;left:0;top:0}
.brand-mark{position:absolute;left:97px;top:12px;width:62px;height:62px;border-radius:50%;border:7px solid var(--grey-mark)}
.brand-name{position:absolute;left:0;top:95px;width:255px;text-align:center;font-family:'Montserrat',sans-serif;font-weight:600;font-size:13.5px;color:var(--grey-text);white-space:nowrap}
.contact-chip{position:absolute;top:25px;display:flex;align-items:center;gap:8px;font-size:12px;color:var(--grey-dark)}
.contact-chip b{font-weight:400;font-size:13.5px}
.icon-dot{width:32px;height:32px;border-radius:50%;background:var(--yellow);display:flex;align-items:center;justify-content:center;flex:none}

.hero{position:absolute;left:0;top:85px;width:1200px;height:426px;background:
  radial-gradient(ellipse 260px 200px at 300px 220px,rgba(74,78,86,.28),transparent 70%),
  linear-gradient(135deg,var(--hero-a),var(--hero-b) 60%,var(--hero-c))}
.side-nav{position:absolute;right:58px;top:243px;list-style:none;z-index:2}
.side-nav::after{content:"";position:absolute;right:0;top:10px;width:1px;height:113px;background:var(--grey-dark);opacity:.5}
.side-nav li{position:relative;height:28.2px;padding-right:14px;text-align:right;font-family:'Montserrat',sans-serif;font-weight:600;font-size:13px;color:var(--grey-dark)}
.side-nav li::after{content:"";position:absolute;right:-4px;top:6px;width:7px;height:7px;border:1px solid var(--grey-dark);border-radius:50%;background:var(--white);z-index:1}
.side-nav li.active{color:var(--yellow)}
.side-nav li.active::after{background:var(--yellow);border-color:var(--yellow)}

.section-title{position:absolute;top:578px;font-family:'Montserrat',sans-serif;font-weight:700;font-size:28px;color:var(--grey-text);letter-spacing:.3px;white-space:nowrap}
.field{position:absolute;left:141px;width:427px;border:1px solid var(--grey-line);font-size:12px;color:var(--grey-text);padding:10px 9px}
.field i{font-style:normal;color:#e53935}
.submit{position:absolute;left:141px;top:894px;width:104px;height:38px;background:var(--yellow);font-family:'Montserrat',sans-serif;font-weight:700;font-size:12.5px;color:var(--grey-dark);display:flex;align-items:center;justify-content:center;gap:5px}
.divider{position:absolute;left:598px;top:590px;width:1px;height:355px;background:#e4e4e4}
.map{position:absolute;left:631px;top:636px;width:427px;height:295px;background:linear-gradient(160deg,var(--map-a),var(--map-b));border:1px solid var(--grey-line)}

.info{position:absolute;top:1045px;display:flex;align-items:center;gap:10px;font-size:11.5px;line-height:14px;color:var(--grey-dark)}
.info strong{font-weight:700}

.site-footer{position:absolute;left:0;top:1119px;width:1200px;height:42px;background:var(--footer);color:var(--white);font-size:11.5px}
.site-footer p{position:absolute;left:141px;top:14px}
.social{position:absolute;top:6px;width:29px;height:29px;border:1.5px solid var(--white);border-radius:50%}
</style>
</head>
<body>

<header class="site-header">
  <div class="contact-chip" style="left:652px"><span class="icon-dot"><svg width="14" height="14" viewBox="0 0 24 24"><path fill="#3a3a3a" d="M6.6 10.8a15 15 0 0 0 6.6 6.6l2.2-2.2c.3-.3.7-.4 1-.2 1.1.4 2.3.6 3.6.6.6 0 1 .4 1 1V20c0 .6-.4 1-1 1A17 17 0 0 1 3 4c0-.6.4-1 1-1h3.5c.6 0 1 .4 1 1 0 1.3.2 2.5.6 3.6.1.3 0 .7-.2 1z"/></svg></span><span>Phone : <b>+1 555-014-2837</b></span></div>
  <div class="contact-chip" style="left:869px"><span class="icon-dot"><svg width="14" height="12" viewBox="0 0 24 18"><rect x="1.5" y="1.5" width="21" height="15" rx="1.5" fill="none" stroke="#3a3a3a" stroke-width="2"/><path d="M2 2l10 8 10-8" fill="none" stroke="#3a3a3a" stroke-width="2"/></svg></span><span>Email : <b>info@brightwellps.com</b></span></div>
</header>

<div class="brand-tab">
  <svg width="255" height="126" viewBox="0 0 255 126"><path d="M0 85 H255 L222 122 Q219 126 213 126 H42 Q36 126 33 122 Z" fill="#fff"/></svg>
  <span class="brand-mark"></span>
  <div class="brand-name">Brightwell Panes &amp; Stoneworks</div>
</div>

<section class="hero" role="img" aria-label="Muted photo of business charts and papers with a dark envelope and telephone illustration"></section>

<ul class="side-nav">
  <li>Home</li>
  <li>About Us</li>
  <li>Projects</li>
  <li>News</li>
  <li class="active">Contact Us</li>
</ul>

<h2 class="section-title" style="left:140px">How Can We Help You?</h2>
<div class="field" style="top:636px;height:35px">Name <i>*</i></div>
<div class="field" style="top:680px;height:35px">Email <i>*</i></div>
<div class="field" style="top:724px;height:35px">Phone</div>
<div class="field" style="top:769px;height:113px">Message <i>*</i></div>
<div class="submit">Submit <svg width="14" height="8" viewBox="0 0 14 8"><path d="M0 4h12M9 1l3 3-3 3" fill="none" stroke="#3a3a3a" stroke-width="1.8"/></svg></div>

<div class="divider"></div>

<h2 class="section-title" style="left:631px">Brightwell Panes &amp; Stoneworks</h2>
<div class="map" role="img" aria-label="Road map of eastern Nebraska showing the office location"></div>

<div class="info" style="left:300px"><span class="icon-dot"><svg width="10" height="14" viewBox="0 0 10 14"><path d="M5 0a5 5 0 0 0-5 5c0 4 5 9 5 9s5-5 5-9a5 5 0 0 0-5-5z" fill="#3a3a3a"/><circle cx="5" cy="5" r="1.8" fill="#f7ec3b"/></svg></span><span>1234 Lorem Ipsum is simply my<br>text of the printing and type</span></div>
<div class="info" style="left:564px"><span class="icon-dot"><svg width="14" height="14" viewBox="0 0 24 24"><path fill="#3a3a3a" d="M6.6 10.8a15 15 0 0 0 6.6 6.6l2.2-2.2c.3-.3.7-.4 1-.2 1.1.4 2.3.6 3.6.6.6 0 1 .4 1 1V20c0 .6-.4 1-1 1A17 17 0 0 1 3 4c0-.6.4-1 1-1h3.5c.6 0 1 .4 1 1 0 1.3.2 2.5.6 3.6.1.3 0 .7-.2 1z"/></svg></span><span><strong>Phone</strong><br>+1 555-014-2837</span></div>
<div class="info" style="left:759px"><span class="icon-dot"><svg width="15" height="11" viewBox="0 0 24 18"><rect x="1" y="1" width="22" height="16" rx="1.5" fill="#3a3a3a"/><path d="M2 2l10 8 10-8" fill="none" stroke="#f7ec3b" stroke-width="1.6"/></svg></span><span><strong>Email</strong><br>info@brightwellps.com</span></div>

<footer class="site-footer">
  <p>Copyright © 2018 Brightwell Panes &amp; Stoneworks. All Rights Reserved.</p>
  <span class="social" style="left:925px"></span>
  <span class="social" style="left:960px"></span>
  <span class="social" style="left:995px"></span>
  <span class="social" style="left:1030px"></span>
</footer>

</body>
</html>
```